" Somos fabricantes e distribuidores de Medidores de Vazao (Hidrometros, bombas Dosadoras, unidades Dosadoras de aditivos), etc. Já estamos no mercado há 18 anos. "

```html
<!DOCTYPE html>
<html lang="pt-BR">
<head>
<meta charset="UTF-8">
<title>Envelope Carta – Vazora</title>
<link rel="stylesheet" href="https://fonts.googleapis.com/css2?family=Montserrat:wght@500;800&family=Roboto+Mono:wght@400&family=Roboto:wght@500&display=swap">
<style>
  :root {
    --backdrop: #9b9985;
    --paper: #f7f7f7;
    --paper-edge: #e4e4e4;
    --ink-black: #151515;
    --ink-charcoal: #3a3a3a;
    --brand-yellow: #f2b51c;
    --brand-grey: #3c3c3c;
    --tagline-grey: #8a8a8a;
    --title-white: #f4f4f0;
  }
  * { margin: 0; padding: 0; box-sizing: border-box; }
  html, body { width: 1200px; height: 1200px; overflow: hidden; }
  body {
    background: var(--backdrop);
    position: relative;
    font-family: "Montserrat", sans-serif;
  }
  .sheet-title {
    position: absolute;
    top: 118px; left: 0; width: 1200px;
    text-align: center;
    font-family: "Roboto Mono", monospace;
    font-size: 36px;
    letter-spacing: 4px;
    color: var(--title-white);
  }
  .envelope {
    position: absolute;
    box-shadow: 0 4px 10px rgba(0,0,0,0.25);
  }
  .envelope-back {
    left: 77px; top: 353px; width: 739px; height: 360px;
    background: linear-gradient(180deg, var(--paper) 0%, #ffffff 55%, var(--paper-edge) 100%);
    overflow: hidden;
  }
  .envelope-back .flap { position: absolute; left: 0; top: 0; }
  .envelope-back .faint-mark {
    position: absolute; left: 10px; top: 150px;
    width: 300px; height: 300px; border-radius: 50%;
    background: radial-gradient(circle, rgba(0,0,0,0.00) 40%, rgba(0,0,0,0.06) 41%, rgba(0,0,0,0.05) 70%, rgba(0,0,0,0) 71%);
  }
  .sender-address {
    position: absolute; left: 96px; top: 639px;
    font-family: "Roboto", sans-serif;
    font-weight: 500;
    font-size: 13px;
    line-height: 22px;
    color: var(--ink-charcoal);
  }
  .brand {
    position: absolute;
    text-align: center;
  }
  .brand-row {
    display: flex; align-items: center; justify-content: center; gap: 12px;
  }
  .brand-dot {
    border-radius: 50%;
    background: var(--brand-yellow);
  }
  .brand-name {
    font-weight: 800;
    letter-spacing: 1px;
    line-height: 1;
  }
  .brand-tagline {
    font-family: "Montserrat", sans-serif;
    font-weight: 500;
    letter-spacing: 4px;
    color: var(--tagline-grey);
  }
  .brand-on-back { left: 570px; top: 610px; width: 240px; }
  .brand-on-back .brand-dot { width: 22px; height: 22px; }
  .brand-on-back .brand-name { font-size: 50px; color: var(--brand-grey); }
  .brand-on-back .brand-tagline { font-size: 9px; margin-top: 6px; }

  .envelope-front {
    left: 350px; top: 763px; width: 783px; height: 360px;
    background: radial-gradient(ellipse at 50% 35%, #3d3d3d 0%, #1d1d1d 55%, var(--ink-black) 100%);
  }
  .brand-on-front { left: 150px; top: 180px; width: 483px; }
  .brand-on-front .brand-dot { width: 26px; height: 26px; }
  .brand-on-front .brand-name { font-size: 58px; color: #f0f0f0; }
  .brand-on-front .brand-tagline { font-size: 11px; margin-top: 10px; color: #b0b0b0; letter-spacing: 5px; }
</style>
</head>
<body>
  <h1 class="sheet-title">ENVELOPE CARTA</h1>

  <div class="envelope envelope-back">
    <svg class="flap" width="739" height="150" viewBox="0 0 739 150" aria-hidden="true">
      <defs>
        <radialGradient id="flapShade" cx="50%" cy="20%" r="70%">
          <stop offset="0" stop-color="#444"/>
          <stop offset="1" stop-color="#111"/>
        </radialGradient>
      </defs>
      <path d="M0 0 H739 V8 L680 118 Q670 136 650 136 H89 Q69 136 59 118 L0 8 Z" fill="url(#flapShade)"/>
    </svg>
    <div class="faint-mark" role="img" aria-label="faint brand symbol decoration"></div>
  </div>
  <p class="sender-address">AV. SUA RUA AQUI, 1320 | BAIRRO - CIDADE/UF<br>CEP: 09090-090</p>
  <div class="brand brand-on-back">
    <div class="brand-row"><span class="brand-dot"></span><span class="brand-name">VAZORA</span></div>
    <div class="brand-tagline">EQUIPAMENTOS INDUSTRIAIS</div>
  </div>

  <div class="envelope envelope-front">
    <div class="brand brand-on-front">
      <div class="brand-row"><span class="brand-dot"></span><span class="brand-name">VAZORA</span></div>
      <div class="brand-tagline">EQUIPAMENTOS INDUSTRIAIS</div>
    </div>
  </div>
</body>
</html>
```